Luxury WordPress Website for CORALBASINS

I need a professional WordPress website for Coral Basins. The site should be modern, visually appealing, and user-friendly, reflecting the brand’s luxury and premium identity. It must include a homepage, product/service pages, contact form, and be responsive on both desktop and mobile devices. The design should allow for easy updates and integration of future content, while maintaining a polished and professional look.

Target Market(s)

swimmingpool & spa

Industry/Entity Type

Swimmingpool

Coding

Coded - Design and coding required

Font styles to use
Other font styles liked:
• HaboroSoft

Requirements
Must have
• Exclusive appearance
Nice to have
• • A logo that subtly incorporates water or pool elements. • A color palette that reflects luxury, elegance, and relaxation. • Clean and modern typography that is easy to read across all media. • Iconography or design elements that convey premium quality. • A versatile design that can be adapted for social media, merchandise, and promotional materials. • Optional: A tagline that emphasizes luxury and high-end pool experiences.

```html
<!DOCTYPE html>
<html lang="en">
<head>
<meta charset="UTF-8">
<title>Coral Basins — Pool Design</title>
<link href="https://fonts.googleapis.com/css2?family=Lexend:wght@700;800&family=Nunito:wght@400;500;600;700&display=swap" rel="stylesheet">
<style>
:root{
  --bg:#f5f8f7;
  --white:#ffffff;
  --ink:#0f1f1c;
  --text:#2f4a47;
  --muted:#2c6e6a;
  --line:#e1e7e5;
  --blue:#1e4dff;
  --cyan:#3ad0e6;
  --water-1:#3cc3e0;
  --water-2:#1d8fb8;
  --deck:#d9c7ad;
}
*{margin:0;padding:0;box-sizing:border-box}
html,body{width:1200px;height:692px;overflow:hidden}
body{background:var(--bg);font-family:"Nunito",sans-serif;color:var(--ink);position:relative}
.site-header{position:absolute;left:0;top:0;width:1200px;height:65px;background:var(--white);box-shadow:0 1px 4px rgba(0,0,0,.08);z-index:3}
.brand{position:absolute;left:154px;top:15px;display:flex;align-items:center;gap:9px}
.brand-mark{width:35px;height:35px;border-radius:6px;background:linear-gradient(135deg,#2a8cff,#1e4dff)}
.brand-name{font-size:13px;font-weight:600;color:var(--ink)}
.main-nav{position:absolute;left:298px;top:25px;display:flex;gap:23px;font-size:10.5px;color:var(--text)}
.btn{display:inline-flex;align-items:center;justify-content:center;border-radius:5px;font-weight:600;text-decoration:none}
.btn-primary{background:linear-gradient(90deg,var(--blue),var(--cyan));color:var(--white);box-shadow:0 3px 8px rgba(30,77,255,.2)}
.btn-ghost{background:var(--white);border:1px solid #d3d9d8;color:var(--ink)}
.header-cta{position:absolute;left:949px;top:20px;width:110px;height:25px;font-size:10.5px}
.hero-title{position:absolute;left:154px;top:133px;width:430px;font-family:"Lexend",sans-serif;font-weight:800;font-size:36px;line-height:44px;letter-spacing:-.3px;color:var(--ink)}
.hero-lead{position:absolute;left:154px;top:280px;width:420px;font-size:12.5px;line-height:21px;color:var(--text)}
.hero-actions{position:absolute;left:154px;top:343px;display:flex;gap:12px}
.hero-actions .btn{height:38px;font-size:11.5px}
.hero-actions .btn-primary{width:133px}
.hero-actions .btn-ghost{width:112px}
.hero-visual{position:absolute;left:600px;top:90px;width:390px;height:400px;border-radius:48% 52% 45% 55%/50% 45% 55% 50%;background:radial-gradient(circle at 55% 45%,var(--water-1) 0%,var(--water-2) 55%,var(--deck) 72%,rgba(245,248,247,0) 74%)}
.section-title{position:absolute;left:154px;top:444px;font-size:21px;font-weight:500;color:var(--ink)}
.service-grid{position:absolute;left:154px;top:494px;display:flex;gap:18px;z-index:2}
.service-card{width:290px;height:151px;background:var(--white);border:1px solid var(--line);border-radius:7px;padding:20px 18px;box-shadow:0 1px 3px rgba(0,0,0,.05)}
.service-icon{width:20px;height:20px;display:block}
.service-card h3{margin-top:12px;font-size:14px;font-weight:500;color:var(--ink)}
.service-card p{margin-top:8px;font-size:11px;line-height:18px;color:var(--muted)}
</style>
</head>
<body>
<header class="site-header">
  <div class="brand"><span class="brand-mark"></span><span class="brand-name">Coral Basins</span></div>
  <nav class="main-nav"><span>Home</span><span>Services</span><span>Portfolio</span><span>About</span><span>Contact</span></nav>
  <a class="btn btn-primary header-cta">Book Consultation</a>
</header>

<h1 class="hero-title">Pool design that transforms outdoor living.</h1>
<p class="hero-lead">We design, build and maintain premium swimming pools and spas — tailored to your property and lifestyle.</p>
<div class="hero-actions">
  <a class="btn btn-primary">Book Consultation</a>
  <a class="btn btn-ghost">View Portfolio</a>
</div>

<div class="hero-visual" role="img" aria-label="Aerial view of a curved turquoise swimming pool with a sandy deck and palm trees"></div>

<h2 class="section-title">Our Services</h2>
<section class="service-grid">
  <article class="service-card">
    <svg class="service-icon" viewBox="0 0 20 20"><path d="M3 17 L15 4 L17 6 L5 18 Z" fill="#2a9d6a"/><path d="M3 17 L2 19 L5 18 Z" fill="#1d5b45"/></svg>
    <h3>Custom Pool Design</h3>
    <p>Bespoke pool concepts, 3D renderings and material selection for a unique outdoor living space.</p>
  </article>
  <article class="service-card">
    <svg class="service-icon" viewBox="0 0 20 20"><path d="M4 4 L16 16 M16 4 L4 16" stroke="#8a3b4a" stroke-width="3" stroke-linecap="round"/><rect x="2" y="2" width="5" height="4" rx="1" fill="#8c8c96"/><rect x="13" y="2" width="5" height="4" rx="1" fill="#8c8c96"/></svg>
    <h3>Build &amp; Construction</h3>
    <p>Precision construction, premium materials, and certified installers to deliver lasting quality.</p>
  </article>
  <article class="service-card">
    <svg class="service-icon" viewBox="0 0 20 20"><rect x="3" y="6" width="14" height="9" rx="4.5" transform="rotate(-35 10 10)" fill="#a970f0"/></svg>
    <h3>Maintenance &amp; Renovation</h3>
    <p>Preventive maintenance plans, seasonal servicing, and high-quality renovation work.</p>
  </article>
</section>
</body>
</html>
```